Corvelle Strategies business card

I need a business card for my new strategic consulting LLC, Corvelle Strategies. We specialize in helping people who care about broadband technology and telecommunications policy, and we're based in Washington DC. I'm looking for a card that says smart, credible, future-facing and signals a high level of expertise. It's DC, so there's clearly a limit to how crazy we can go with this card, but I am looking for a design that reflects a company that is comfortable with technology, policy, and having a little bit fun. I'm uploading my logo below, and I'd like to have it be part of the card design in some fashion.
Target Market(s)
Telecommunications and technology policy professionals
Industry/Entity Type
Technology policy
Contact Information for Business Card
Name of business, my name (Glen Mosswater), email (glen@corvellestrategies-example.com) , phone number (202-555-0148)phone number

```html
<!DOCTYPE html>
<html lang="en">
<head>
<meta charset="utf-8">
<title>Corvelle Strategies – Business Card</title>
<link rel="stylesheet" href="https://fonts.googleapis.com/css2?family=Montserrat:wght@500;600;700&display=swap">
<style>
  :root {
    --page-bg: #e6e6e6;
    --card-blue: #06529e;
    --forest-blue: #0b4a92;
    --forest-deep: #08427f;
    --gold: #f3b233;
    --white: #ffffff;
  }
  * { box-sizing: border-box; margin: 0; padding: 0; }
  html, body {
    width: 1200px; height: 1200px; overflow: hidden;
    background: var(--page-bg);
    font-family: "Montserrat", sans-serif;
  }
  .card {
    position: absolute; left: 206px; width: 787px; height: 450px;
    background: var(--card-blue); overflow: hidden;
  }
  .card--front { top: 105px; }
  .card--back { top: 645px; }
  .forest {
    position: absolute; left: 0; right: 0; bottom: 0; height: 200px;
    background: linear-gradient(to bottom, rgba(11,74,146,0) 0%, var(--forest-blue) 45%, var(--forest-deep) 100%);
  }
  .brand {
    position: absolute; left: 0; right: 0; top: 150px;
    display: flex; align-items: center; justify-content: center; gap: 18px;
  }
  .brand__name {
    color: var(--white); font-weight: 700; font-size: 52px; letter-spacing: 1px;
  }
  .brand__dot {
    width: 44px; height: 44px; border-radius: 50%; background: var(--gold);
  }
  .tagline {
    position: absolute; left: 0; right: 0; top: 302px; text-align: center;
    color: var(--gold); font-weight: 600; font-size: 23px; letter-spacing: 1.4px;
  }
  .person { position: absolute; left: 81px; top: 82px; color: var(--white); }
  .person__name { font-weight: 600; font-size: 29px; letter-spacing: 2px; text-transform: uppercase; }
  .person__role { margin-top: 10px; font-weight: 600; font-size: 22px; letter-spacing: 0.6px; }
  .divider {
    position: absolute; left: 0; top: 168px; width: 551px; height: 3px; background: var(--gold);
  }
  .contacts { position: absolute; left: 80px; top: 184px; list-style: none; color: var(--white); }
  .contacts li {
    display: flex; align-items: center; gap: 8px; height: 46px;
    font-weight: 500; font-size: 23px;
  }
  .contacts svg { width: 20px; height: 20px; flex: none; fill: var(--gold); }
</style>
</head>
<body>

<section class="card card--front" aria-label="Card front">
  <div class="forest" role="img" aria-label="Faint pine forest silhouette along the bottom"></div>
  <div class="brand">
    <span class="brand__name">Corvelle Strategies</span>
    <span class="brand__dot"></span>
  </div>
  <p class="tagline">STRATEGY • POLICY • CONNECTIVITY</p>
</section>

<section class="card card--back" aria-label="Card back">
  <div class="forest" role="img" aria-label="Faint pine forest silhouette along the bottom"></div>
  <div class="person">
    <h1 class="person__name">Glen Mosswater</h1>
    <p class="person__role">Founder &amp; Principal</p>
  </div>
  <div class="divider"></div>
  <ul class="contacts">
    <li>
      <svg viewBox="0 0 20 20" aria-hidden="true"><path d="M1 4h18v12H1z M2 5l8 6 8-6" fill="var(--gold)"/><path d="M2 5l8 6 8-6" fill="none" stroke="#06529e" stroke-width="1.6"/></svg>
      glen@corvellestrategies-example.com
    </li>
    <li>
      <svg viewBox="0 0 20 20" aria-hidden="true"><path d="M5 2l3 4-2 2c1 2.5 3.5 5 6 6l2-2 4 3-2 3C9 18 2 11 2 4z"/></svg>
      202-555-0148
    </li>
    <li>
      <svg viewBox="0 0 20 20" aria-hidden="true"><g fill="none" stroke="var(--gold)" stroke-width="1.6"><circle cx="10" cy="10" r="8"/><ellipse cx="10" cy="10" rx="3.5" ry="8"/><path d="M2 10h16M3.5 6h13M3.5 14h13"/></g></svg>
      corvellestrategies-example.com
    </li>
  </ul>
</section>

</body>
</html>
```